Design a cover that embodies the concept of healing by Walking Out of the Fog

Subtitle: How to use tapping, applied kinesiology, and Chinese medicine to heal your body, free your mind and live in peace.

Tapping (Emotional Freedom Technique) is a modern mix of psychology and Chinese medicine that helps people to release the emotions they have inside that are contributing to the depression and anxiety they feel. Applied kinesiology or muscle testing is a biofeedback tool which helps to extract information from the body that can help people to profoundly heal. It can be used to determine whether heavy metals, heavy chemicals, food sensitivities or pathogens are causing the body problems. It can also be used to determine which supplements can help someone heal. This tool also can be used to identify emotions and memories that are also causing someone problems. Lastly, Chinese medicine uses food therapy, herbal formulas, meditation, tai chi (meditative movement), cupping and other tools to help people to be free of depression. This book is written to be information but also details my own personal journey of how I was able to heal from 11 years of heavy depression through the use of these tools.

The heart of the book is about emotional release, emotional freedom and emotional healing. You can surrender, release or let go of emotions and feel better very quickly. This certainly was my experience.

I would like the front and back cover to each be 8.5" x 5.5". I still have to get an ISBN number for the back page as well. Here is the text that I would like on the back cover for now: Millions of people feel the pain, loneliness, and agony of anxiety and depression every day. Many turn to Western medicine in the hopes that a pill will ease the pain and make the problem go away. Oftentimes, this only makes matters worse and doesn’t address the root cause. No one should have to struggle like this when natural answers exist that can address the physical, energetic, emotional, or spiritual causes of anxiety and depression. For 11 long years, Dr. Vance personally struggled with heavy depression until he discovered answers that helped him to completely heal. Walking Out of the Fog is a guide that will help you discover - The two root physical causes of depression and exactly what to do to start healing today - How the negative emotions we have stored within from trauma and bad experiences can drive depression - Tools from Chinese medicine, applied kinesiology, and tapping to help you free your mind and live in peace - An actionable plan to help you let go of the pain, suffering, and negative emotions from your past Whether you feel depressed and anxious or know someone who struggles with these issues, Walking Out of the Fog will transform how you think about depression and will give you the tools to heal so that you can be free and live in peace. Dr. Vance Holbrook is a board-certified acupuncture physician licensed in the state of Florida. He received his training at the Calder Institute of Holistic Practice. He also graduated with a master’s degree in counseling and psychology from Meadowbrook Seminary of Theology. His mission is to help people transform their health and improve the quality of their life naturally. He lives in Orlando, FL where he runs a holistic medical clinic called Bluepine Wellness Center. www.drvanceholbrook-example.com Instagram: drvanceholbrook Facebook: bluepinewellnesscenter

Target Market(s)

Those who suffer from depression and anxiety and want to heal naturally

Industry/Entity Type

Health And Wellness

Requirements
Must have
• My picture should be small and go on the back cover next to the information about me. The front cover would be all graphical. Thank you. On the front cover my name should be posted as "Dr. Vance Holbrook, AP, MA"

```html
<!DOCTYPE html>
<html lang="en">
<head>
<meta charset="utf-8">
<title>Walking Out of the Fog – Cover Spread</title>
<link href="https://fonts.googleapis.com/css2?family=Oswald:wght@400;500&family=Lora:ital,wght@0,400;0,600;1,400&display=swap" rel="stylesheet">
<style>
  :root {
    --frame: #3b3b3b;
    --paper: #ffffff;
    --teal: #4fc4c4;
    --teal-text: #3cbdb8;
    --teal-deep: #1f6f6c;
    --ink: #1c4850;
    --dark: #2e2e2e;
    --yellow: #fde58a;
    --sea-light: #d8ecec;
    --sea: #5fa9b4;
    --sea-deep: #2d6f80;
  }
  * { margin: 0; padding: 0; box-sizing: border-box; }
  html, body { width: 1200px; height: 896px; overflow: hidden; background: var(--frame); }
  .spread {
    position: absolute; left: 24px; top: 26px; width: 1150px; height: 850px;
    background: var(--paper);
  }
  /* Back cover */
  .back { position: absolute; left: 0; top: 0; width: 550px; height: 850px; font-family: "Lora", Georgia, serif; color: var(--ink); }
  .back p { font-size: 14.6px; line-height: 18.4px; text-align: justify; hyphens: auto; }
  .back-intro { position: absolute; left: 24px; top: 42px; width: 506px; }
  .discover-box {
    position: absolute; left: 50px; top: 214px; width: 454px; height: 246px;
    background: var(--yellow); padding: 6px 12px; text-align: center;
  }
  .discover-box .lead { font-size: 15px; line-height: 18.4px; text-align: center; margin-bottom: 12px; }
  .discover-box .lead span { text-decoration: underline; text-underline-offset: 2px; }
  .discover-box ul { list-style: none; }
  .discover-box li { font-size: 15px; line-height: 18.4px; margin-bottom: 13px; }
  .back-closing { position: absolute; left: 24px; top: 476px; width: 506px; }
  .author-box {
    position: absolute; left: 21px; top: 552px; width: 511px; height: 154px;
    background: var(--teal); padding: 10px 4px 0 0;
  }
  .author-photo { position: absolute; left: 5px; top: 12px; width: 86px; height: 128px; background: linear-gradient(160deg, #d9c3a8, #b98f6f 55%, #e7dccb); }
  .author-bio { position: absolute; left: 98px; top: 6px; width: 408px; color: #fff; font-style: italic; font-size: 14.2px !important; line-height: 18.4px !important; }
  .contacts { position: absolute; left: 24px; top: 756px; font-size: 14px; line-height: 18.5px; }
  .contacts strong { font-weight: 600; }
  /* Spine */
  .spine { position: absolute; left: 550px; top: 0; width: 50px; height: 850px; }
  .spine-title {
    position: absolute; left: 0; top: 58px; width: 50px; height: 430px;
    writing-mode: vertical-rl; font-family: "Oswald", sans-serif; font-weight: 500;
    font-size: 36px; line-height: 50px; color: var(--teal-text); text-align: center; letter-spacing: 0.5px;
  }
  .spine-band { position: absolute; left: 0; top: 498px; width: 50px; height: 336px; background: var(--teal); }
  .spine-author {
    position: absolute; left: 0; top: 6px; width: 50px; height: 324px;
    writing-mode: vertical-rl; font-family: "Oswald", sans-serif; font-size: 25px; line-height: 50px;
    color: #fff; text-align: center;
  }
  /* Front cover */
  .front { position: absolute; left: 600px; top: 0; width: 550px; height: 850px; background: #fbfbf8; overflow: hidden; font-family: "Oswald", sans-serif; text-align: center; }
  .front-photo {
    position: absolute; left: 0; top: 220px; width: 550px; height: 630px;
    background: linear-gradient(180deg, #fbfbf8 0%, var(--sea-light) 18%, #a9d3d8 38%, var(--sea) 62%, var(--sea-deep) 100%);
  }
  .front-author { position: absolute; left: 0; top: 44px; width: 550px; font-size: 39px; color: var(--teal-text); letter-spacing: 0.3px; }
  .front-rule { position: absolute; left: 96px; top: 92px; width: 380px; height: 2px; background: var(--teal-text); }
  .front-title {
    position: absolute; left: 0; top: 130px; width: 550px; font-size: 94px; line-height: 98px; font-weight: 500;
    background: linear-gradient(180deg, #5bc3bf, var(--teal-deep)); -webkit-background-clip: text; background-clip: text; color: transparent;
  }
  .front-subtitle { position: absolute; left: 0; top: 360px; width: 550px; }
  .front-subtitle .dark { display: block; color: var(--dark); }
  .front-subtitle .accent { display: block; color: var(--teal-text); font-size: 26px; line-height: 32px; }
  .front-subtitle .lead { font-size: 34px; line-height: 38px; }
  .front-subtitle .tail { font-size: 29px; line-height: 37px; margin-top: 2px; }
</style>
</head>
<body>
  <div class="spread">
    <section class="back">
      <p class="back-intro">Millions of people feel the pain, loneliness, and agony of anxiety and depression every day. Many turn to Western medicine in the hopes that a pill will ease the pain and make the problem go away. Oftentimes, this only makes matters worse and doesn’t address the root cause. No one should have to struggle like this when natural answers exist that can address the physical, energetic, emotional, or spiritual causes of anxiety and depression.<br>For 11 long years, Dr. Vance personally struggled with heavy depression until he discovered answers that helped him to completely heal.</p>
      <div class="discover-box">
        <p class="lead"><span>Walking Out of the Fog</span><br><span>is a guide that will help you discover:</span></p>
        <ul>
          <li>- The two root physical causes of depression and exactly what to do to start healing today.</li>
          <li>- How the negative emotions we have stored within from trauma and bad experiences can drive depression.</li>
          <li>- Tools from Chinese medicine, applied kinesiology, and tapping to help you free your mind and live in peace.</li>
          <li>- An actionable plan to help you let go of the pain, suffering, and negative emotions from your past.</li>
        </ul>
      </div>
      <p class="back-closing">Whether you feel depressed and anxious or know someone who struggles with these issues, Walking Out of the Fog will transform how you think about depression and will give you the tools to heal so that you can be free and live in peace.</p>
      <div class="author-box">
        <div class="author-photo" role="img" aria-label="Small portrait photo of the author"></div>
        <p class="author-bio">Dr. Vance Holbrook is a board-certified acupuncture physician licensed in the state of Florida. He received his training at the Calder Institute of Holistic Practice. He also graduated with a master’s degree in counseling and psychology from Meadowbrook Seminary of Theology. His mission is to help people transform their health and improve the quality of their life naturally. He lives in Orlando, FL where he runs a holistic medical clinic called Bluepine Wellness Center.</p>
      </div>
      <div class="contacts">
        <strong>www.drvanceholbrook-example.com</strong><br>
        Instagram: <strong>drvanceholbrook</strong><br>
        Facebook: <strong>bluepinewellnesscenter</strong>
      </div>
    </section>

    <section class="spine">
      <div class="spine-title">WALKING OUT OF THE FOG</div>
      <div class="spine-band"><div class="spine-author">DR. VANCE HOLBROOK, AP, MA</div></div>
    </section>

    <section class="front">
      <div class="front-photo" role="img" aria-label="Photo of an open hand reaching toward a sparkling turquoise sea"></div>
      <div class="front-author">DR. VANCE HOLBROOK, AP, MA</div>
      <div class="front-rule"></div>
      <h1 class="front-title">WALKING OUT<br>OF THE FOG</h1>
      <div class="front-subtitle">
        <span class="dark lead">HOW TO USE</span>
        <span class="accent">TAPPING, APPLIED KINESIOLOGY,</span>
        <span class="accent">AND CHINESE MEDICINE</span>
        <span class="dark tail">TO HEAL YOUR BODY, FREE YOUR MIND<br>AND LIVE IN PEACE</span>
      </div>
    </section>
  </div>
</body>
</html>
```